Online Marketing Agency Website

We are an online marketing agency that specializes in search marketing (SEM) for businesses of all sizes. Our core services include local search marketing, seo, paid search, paid social, graphic design, video production/editing and website design. We have an existing website that we launched a number of years ago but it's very outdated and we're currently too busy to design a new version.

Target Market(s)

Any business that needs online marketing services with an emphasis on search marketing.

Industry/Entity Type

Ad Agency

Number of Pages Required

4 page

Font styles to use
Sans Serif

Requirements
Must have
• Home page, interior page, blog page, contact us page.
Look and feel should be modern and clean and easy to navigate.
Sections for call outs for specific services: Business Marketing Strategy, Content Creation and Marketing, Graphic & Publication Design, Pay Per Click (PPC) Management, Search Engine Optimization, Social Media Management, Video Production & Editing, Website Hosting & Management, Website Design & Development
Use color from logo that was uploaded.

```html
<!DOCTYPE html>
<html lang="en">
<head>
<meta charset="utf-8">
<title>Latest Blog – Liftwave Media</title>
<link rel="stylesheet" href="https://fonts.googleapis.com/css2?family=Poppins:wght@400;500;600;700;800&display=swap">
<style>
:root{
  --accent:#ff4a0f;
  --ink:#2f2f2f;
  --text:#4a4a4a;
  --muted:#9a9a9a;
  --line:#e8e8e8;
  --footer:#333333;
  --footer-line:#454545;
  --white:#ffffff;
  --soft:#ececec;
}
*{box-sizing:border-box;margin:0;padding:0}
html,body{width:1200px;height:2496px;overflow:hidden}
body{position:relative;background:var(--white);font-family:"Poppins",sans-serif;color:var(--text)}
a{color:inherit;text-decoration:none}

.site-header{position:absolute;left:0;top:0;width:1200px;height:130px}
.brand{position:absolute;left:86px;top:28px;text-align:center;width:146px}
.brand-dot{display:block;width:26px;height:26px;border-radius:50%;background:var(--accent);margin:0 auto 10px}
.brand-name{font-size:18px;font-weight:600;color:var(--ink);line-height:20px;letter-spacing:.2px}
.brand-tag{font-size:11px;font-weight:400;color:var(--ink);line-height:14px}
.main-nav{position:absolute;right:150px;top:58px;display:flex;gap:30px;font-size:12.5px;font-weight:500;color:var(--ink);letter-spacing:.2px}
.main-nav .active{color:var(--accent);position:relative}
.active-bar{position:absolute;left:850px;top:0;width:48px;height:3px;background:var(--accent)}
.search-btn{position:absolute;left:1069px;top:47px;width:42px;height:42px;border-radius:50%;background:var(--soft);display:flex;align-items:center;justify-content:center}

.page-title{position:absolute;left:0;top:144px;width:1200px;text-align:center}
.page-title h1{font-size:53px;font-weight:700;line-height:64px;color:var(--ink);letter-spacing:1px}
.page-title h1 span{color:var(--accent)}
.crumbs{font-size:17px;color:var(--ink);margin-top:2px;display:flex;justify-content:center;align-items:center;gap:14px}
.crumbs .home{display:flex;align-items:center;gap:5px}
.divider{position:absolute;left:97px;top:271px;width:1022px;height:1px;background:var(--line)}

.blog-grid{position:absolute;left:89px;top:352px;display:grid;grid-template-columns:repeat(3,324px);grid-auto-rows:438px;column-gap:25px;row-gap:20px}
.post-card{background:var(--white);box-shadow:0 4px 22px rgba(0,0,0,.07);border-radius:4px;padding:12px 12px 0}
.post-media{height:202px;border-radius:4px}
.m1{background:linear-gradient(135deg,#4a3a32,#d8d2cc 60%,#8a7466)}
.m2{background:linear-gradient(135deg,#2c2622,#8a5a34 55%,#3e2c20)}
.m3{background:linear-gradient(135deg,#3c3c3e,#8c8f93 55%,#d9d3cc)}
.m4{background:linear-gradient(135deg,#d7d2cb,#5a4a3e 55%,#2a2a2c)}
.m5{background:linear-gradient(135deg,#e0e0e0,#3a3a3e 50%,#a06a44)}
.m6{background:linear-gradient(135deg,#1f1f21,#3a3536 50%,#c4622a)}
.m7{background:linear-gradient(135deg,#9a6a44,#e9e6e2 50%,#5b3d28)}
.m8{background:linear-gradient(135deg,#5a5a5c,#e8e6e4 50%,#3a3a3c)}
.m9{background:linear-gradient(135deg,#d8d8d6,#3a3a3c 55%,#7a7a78)}
.post-body{padding:20px 18px 0}
.post-date{font-size:14px;font-weight:500;color:var(--accent);line-height:18px}
.post-title{font-size:15px;font-weight:700;color:var(--ink);line-height:20px;letter-spacing:.9px;text-transform:uppercase;margin-top:9px}
.post-excerpt{font-size:14.5px;color:var(--text);line-height:20px;margin-top:21px}
.post-comment{display:flex;align-items:center;gap:5px;font-size:12.5px;font-weight:600;color:var(--muted);margin-top:23px;letter-spacing:.2px}

.pager{position:absolute;left:424px;top:1772px;height:32px;display:flex;align-items:center;font-size:14.5px;color:var(--ink)}
.pager .prev{width:77px;height:30px;border-radius:15px;background:var(--soft);display:flex;align-items:center;justify-content:center;margin-right:17px}
.pager .num{margin-right:22px}
.pager .current{width:31px;height:31px;border-radius:50%;background:var(--ink);color:var(--white);display:flex;align-items:center;justify-content:center;margin:0 17px 0 -4px}
.pager .next{width:76px;height:30px;border-radius:15px;background:var(--accent);color:var(--white);display:flex;align-items:center;justify-content:center;font-weight:500;margin-left:0}

.site-footer{position:absolute;left:0;top:1898px;width:1200px;height:598px;background:var(--footer);color:var(--white)}
.newsletter h2{position:absolute;left:0;top:76px;width:1200px;text-align:center;font-size:40px;font-weight:700;line-height:50px;letter-spacing:.5px}
.newsletter h2 span{color:var(--accent)}
.news-form{position:absolute;left:276px;top:142px;width:646px;height:61px;border-radius:31px;background:var(--white);display:flex;align-items:center;padding-left:26px}
.news-form .field{display:flex;align-items:center;gap:11px;font-size:16.5px;color:#6a6a6a}
.news-form .subscribe{position:absolute;right:8px;top:8px;width:160px;height:45px;border-radius:23px;background:var(--accent);color:var(--white);font-size:15px;font-weight:600;display:flex;align-items:center;justify-content:center;letter-spacing:.4px}
.foot-brand{position:absolute;left:148px;top:262px;width:172px;text-align:center}
.foot-brand .brand-name{color:var(--white);font-size:19px}
.foot-brand .brand-tag{color:var(--white);font-size:12px}
.socials{position:absolute;left:165px;top:378px;display:flex;gap:7px}
.socials span{width:37px;height:37px;border-radius:50%;display:block}
.socials .s1{background:#3b5998}.socials .s2{background:#1da1f2}.socials .s3{background:#dd2c1e}
.foot-col{position:absolute;top:269px}
.foot-col h3{font-size:15px;font-weight:600;letter-spacing:.8px;line-height:20px}
.foot-col ul{list-style:none;font-size:14px;line-height:26.6px;color:#e4e4e4}
.col-company{left:405px}.col-company ul{margin-top:14px}
.col-support{left:624px}.col-support ul{margin-top:24px}
.col-contact{left:840px}
.contact-list{list-style:none;margin-top:25px;font-size:14px;color:#e4e4e4;line-height:18px}
.contact-list li{display:flex;gap:11px;margin-bottom:20px}
.contact-list svg{flex:none;margin-top:2px}
.foot-rule{position:absolute;left:0;top:532px;width:1200px;height:1px;background:var(--footer-line)}
.copyright{position:absolute;left:0;top:555px;width:1200px;text-align:center;font-size:13px;letter-spacing:.1px}
.chat-btn{position:absolute;left:1124px;top:505px;width:52px;height:52px;border-radius:50%;background:var(--accent);display:flex;align-items:center;justify-content:center}
</style>
</head>
<body>

<header class="site-header">
  <div class="active-bar"></div>
  <div class="brand">
    <span class="brand-dot"></span>
    <div class="brand-name">LIFTWAVE MEDIA</div>
    <div class="brand-tag">Online Marketing. Elevated</div>
  </div>
  <nav class="main-nav">
    <a href="#">HOME</a><a href="#">SERVICES</a><a href="#">FEATURED WORK</a><a href="#" class="active">BLOG</a><a href="#">ABOUT</a><a href="#">CONTACT</a>
  </nav>
  <div class="search-btn">
    <svg width="16" height="16" viewBox="0 0 16 16"><circle cx="6.5" cy="6.5" r="5" fill="none" stroke="#2f2f2f" stroke-width="1.8"/><line x1="10.2" y1="10.2" x2="14.5" y2="14.5" stroke="#2f2f2f" stroke-width="1.8" stroke-linecap="round"/></svg>
  </div>
</header>

<section class="page-title">
  <h1><span>LATEST</span> BLOG</h1>
  <div class="crumbs">
    <span class="home"><svg width="17" height="14" viewBox="0 0 17 14"><path d="M8.5 0L0 7h2.3v7h4.5V9.5h3.4V14h4.5V7H17z" fill="#2f2f2f"/></svg>Home</span>
    <span>|</span><span>Latest Blog</span>
  </div>
</section>
<div class="divider"></div>

<main class="blog-grid">
  <article class="post-card"><div class="post-media m1" role="img" aria-label="Photo of a hand with a stylus beside a laptop and coffee cup"></div><div class="post-body"><div class="post-date">25-05-2020</div><h2 class="post-title">Some blog heading goes here with desciption below...</h2><p class="post-excerpt">Lorem ipsum dolor sit amet, elit, sed do eiusmod tempor incididunt ut labore et dolore...</p><div class="post-comment"><svg width="15" height="13" viewBox="0 0 15 13"><path d="M7.5 0C3.4 0 0 2.5 0 5.6c0 1.6.9 3 2.3 4L1.6 13l3.3-2c.8.2 1.7.3 2.6.3 4.1 0 7.5-2.5 7.5-5.7S11.6 0 7.5 0z" fill="#b8b8b8"/></svg>ADD COMMENT</div></div></article>
  <article class="post-card"><div class="post-media m2" role="img" aria-label="Photo of two people working at a wooden table with a laptop"></div><div class="post-body"><div class="post-date">25-05-2020</div><h2 class="post-title">Some blog heading goes here with desciption below...</h2><p class="post-excerpt">Lorem ipsum dolor sit amet, elit, sed do eiusmod tempor incididunt ut labore et dolore...</p><div class="post-comment"><svg width="15" height="13" viewBox="0 0 15 13"><path d="M7.5 0C3.4 0 0 2.5 0 5.6c0 1.6.9 3 2.3 4L1.6 13l3.3-2c.8.2 1.7.3 2.6.3 4.1 0 7.5-2.5 7.5-5.7S11.6 0 7.5 0z" fill="#b8b8b8"/></svg>ADD COMMENT</div></div></article>
  <article class="post-card"><div class="post-media m3" role="img" aria-label="Photo of a businessman at a laptop with colleagues behind"></div><div class="post-body"><div class="post-date">25-05-2020</div><h2 class="post-title">Some blog heading goes here with desciption below...</h2><p class="post-excerpt">Lorem ipsum dolor sit amet, elit, sed do eiusmod tempor incididunt ut labore et dolore...</p><div class="post-comment"><svg width="15" height="13" viewBox="0 0 15 13"><path d="M7.5 0C3.4 0 0 2.5 0 5.6c0 1.6.9 3 2.3 4L1.6 13l3.3-2c.8.2 1.7.3 2.6.3 4.1 0 7.5-2.5 7.5-5.7S11.6 0 7.5 0z" fill="#b8b8b8"/></svg>ADD COMMENT</div></div></article>
  <article class="post-card"><div class="post-media m4" role="img" aria-label="Photo of colleagues reviewing charts on a laptop"></div><div class="post-body"><div class="post-date">25-05-2020</div><h2 class="post-title">Some blog heading goes here with desciption below...</h2><p class="post-excerpt">Lorem ipsum dolor sit amet, elit, sed do eiusmod tempor incididunt ut labore et dolore...</p><div class="post-comment"><svg width="15" height="13" viewBox="0 0 15 13"><path d="M7.5 0C3.4 0 0 2.5 0 5.6c0 1.6.9 3 2.3 4L1.6 13l3.3-2c.8.2 1.7.3 2.6.3 4.1 0 7.5-2.5 7.5-5.7S11.6 0 7.5 0z" fill="#b8b8b8"/></svg>ADD COMMENT</div></div></article>
  <article class="post-card"><div class="post-media m5" role="img" aria-label="Photo of three business people talking in an office"></div><div class="post-body"><div class="post-date">25-05-2020</div><h2 class="post-title">Some blog heading goes here with desciption below...</h2><p class="post-excerpt">Lorem ipsum dolor sit amet, elit, sed do eiusmod tempor incididunt ut labore et dolore...</p><div class="post-comment"><svg width="15" height="13" viewBox="0 0 15 13"><path d="M7.5 0C3.4 0 0 2.5 0 5.6c0 1.6.9 3 2.3 4L1.6 13l3.3-2c.8.2 1.7.3 2.6.3 4.1 0 7.5-2.5 7.5-5.7S11.6 0 7.5 0z" fill="#b8b8b8"/></svg>ADD COMMENT</div></div></article>
  <article class="post-card"><div class="post-media m6" role="img" aria-label="Photo of a woman in an orange jacket holding a notebook"></div><div class="post-body"><div class="post-date">25-05-2020</div><h2 class="post-title">Some blog heading goes here with desciption below...</h2><p class="post-excerpt">Lorem ipsum dolor sit amet, elit, sed do eiusmod tempor incididunt ut labore et dolore...</p><div class="post-comment"><svg width="15" height="13" viewBox="0 0 15 13"><path d="M7.5 0C3.4 0 0 2.5 0 5.6c0 1.6.9 3 2.3 4L1.6 13l3.3-2c.8.2 1.7.3 2.6.3 4.1 0 7.5-2.5 7.5-5.7S11.6 0 7.5 0z" fill="#b8b8b8"/></svg>ADD COMMENT</div></div></article>
  <article class="post-card"><div class="post-media m7" role="img" aria-label="Photo of a handshake over a desk with papers and a laptop"></div><div class="post-body"><div class="post-date">25-05-2020</div><h2 class="post-title">Some blog heading goes here with desciption below...</h2><p class="post-excerpt">Lorem ipsum dolor sit amet, elit, sed do eiusmod tempor incididunt ut labore et dolore...</p><div class="post-comment"><svg width="15" height="13" viewBox="0 0 15 13"><path d="M7.5 0C3.4 0 0 2.5 0 5.6c0 1.6.9 3 2.3 4L1.6 13l3.3-2c.8.2 1.7.3 2.6.3 4.1 0 7.5-2.5 7.5-5.7S11.6 0 7.5 0z" fill="#b8b8b8"/></svg>ADD COMMENT</div></div></article>
  <article class="post-card"><div class="post-media m8" role="img" aria-label="Photo of a team joining hands over a meeting table"></div><div class="post-body"><div class="post-date">25-05-2020</div><h2 class="post-title">Some blog heading goes here with desciption below...</h2><p class="post-excerpt">Lorem ipsum dolor sit amet, elit, sed do eiusmod tempor incididunt ut labore et dolore...</p><div class="post-comment"><svg width="15" height="13" viewBox="0 0 15 13"><path d="M7.5 0C3.4 0 0 2.5 0 5.6c0 1.6.9 3 2.3 4L1.6 13l3.3-2c.8.2 1.7.3 2.6.3 4.1 0 7.5-2.5 7.5-5.7S11.6 0 7.5 0z" fill="#b8b8b8"/></svg>ADD COMMENT</div></div></article>
  <article class="post-card"><div class="post-media m9" role="img" aria-label="Photo of three colleagues gathered around a laptop in an office"></div><div class="post-body"><div class="post-date">25-05-2020</div><h2 class="post-title">Some blog heading goes here with desciption below...</h2><p class="post-excerpt">Lorem ipsum dolor sit amet, elit, sed do eiusmod tempor incididunt ut labore et dolore...</p><div class="post-comment"><svg width="15" height="13" viewBox="0 0 15 13"><path d="M7.5 0C3.4 0 0 2.5 0 5.6c0 1.6.9 3 2.3 4L1.6 13l3.3-2c.8.2 1.7.3 2.6.3 4.1 0 7.5-2.5 7.5-5.7S11.6 0 7.5 0z" fill="#b8b8b8"/></svg>ADD COMMENT</div></div></article>
</main>

<nav class="pager">
  <a class="prev" href="#">‹ Prev</a>
  <a class="num" href="#">1</a>
  <span class="current">2</span>
  <a class="num" href="#">3</a>
  <span class="num">...</span>
  <a class="num" href="#">82</a>
  <a class="next" href="#">Next ›</a>
</nav>

<footer class="site-footer">
  <section class="newsletter">
    <h2><span>OUR</span> NEWSLETTER</h2>
    <div class="news-form">
      <span class="field"><svg width="18" height="13" viewBox="0 0 18 13"><rect width="18" height="13" rx="1.5" fill="#c9c9c9"/><path d="M1 1l8 6 8-6" fill="none" stroke="#fff" stroke-width="1.4"/></svg>Enter your email address</span>
      <span class="subscribe">SUBSCRIBE</span>
    </div>
  </section>

  <div class="foot-brand">
    <span class="brand-dot"></span>
    <div class="brand-name">LIFTWAVE MEDIA</div>
    <div class="brand-tag">Online Marketing. Elevated.</div>
  </div>
  <div class="socials">
    <span class="s1" role="img" aria-label="Social profile"></span>
    <span class="s2" role="img" aria-label="Social profile"></span>
    <span class="s3" role="img" aria-label="Social profile"></span>
  </div>

  <div class="foot-col col-company">
    <h3>COMPANY</h3>
    <ul><li>Home</li><li>Our Services</li><li>Featured Work</li><li>Blog</li><li>About</li><li>Contact</li></ul>
  </div>
  <div class="foot-col col-support">
    <h3>SUPPORT</h3>
    <ul><li>Terms of use</li><li>Terms &amp; Conditions</li><li>Privacy Policy</li><li>Returns</li><li>Refunds.</li></ul>
  </div>
  <div class="foot-col col-contact">
    <h3>CONTACT US</h3>
    <ul class="contact-list">
      <li><svg width="13" height="13" viewBox="0 0 13 13"><path d="M2.6 0.5l2 2.4-1.2 1.6c.9 1.9 2.3 3.3 4.2 4.2l1.6-1.2 2.4 2-1 2.2C5.2 11.6 1.4 7.8.5 2.3z" fill="#ff4a0f"/></svg>800-555-0142</li>
      <li><svg width="13" height="10" viewBox="0 0 13 10"><rect width="13" height="10" rx="1" fill="#ff4a0f"/><path d="M1 1l5.5 4.2L12 1" fill="none" stroke="#333" stroke-width="1.2"/></svg>hello@liftwave.example</li>
      <li><svg width="12" height="15" viewBox="0 0 12 15"><path d="M6 0C2.7 0 0 2.6 0 5.8 0 10 6 15 6 15s6-5 6-9.2C12 2.6 9.3 0 6 0z" fill="#ff4a0f"/><circle cx="6" cy="5.8" r="2.1" fill="#333"/></svg>Some address line goes here<br>city name</li>
    </ul>
  </div>

  <div class="foot-rule"></div>
  <p class="copyright">COPYRIGHT © 2020 LIFTWAVE MEDIA LLC. ALL RIGHTS RESERVED.</p>
  <div class="chat-btn">
    <svg width="26" height="22" viewBox="0 0 26 22"><path d="M13 1C6.4 1 1 5 1 10c0 2.6 1.5 5 3.9 6.6L4 21l5-2.6c1.2.3 2.6.5 4 .5 6.6 0 12-4 12-9S19.6 1 13 1z" fill="#fff"/><circle cx="8.5" cy="10" r="1.6" fill="#ff4a0f"/><circle cx="13" cy="10" r="1.6" fill="#ff4a0f"/><circle cx="17.5" cy="10" r="1.6" fill="#ff4a0f"/></svg>
  </div>
</footer>

</body>
</html>
```